We are an Estate agency (Real estate)– looking for Christmas/winter theme leaflet

We are called ‘’HOLLIVERS’’ we are an estate agency based in England. We opened in 2020 in February, few weeks before Covid and we are now known as one of the fastest growing agencies in all of Brighton and Hove.
This is our first Christmas/winter leaflet and this kind of offer!
Offer is: if the client signs with us to sell their home from 1st December 2021 until 7th January 2022 they will receive 50% off HOLLIVERS fees.
I am looking for A5 two-sided leaflet. The first side should contain our branding, the offer. Also, maybe this: ‘’ Let us Treat you this Christmas’’ or maybe on the other side of leaflet, which will contain explanation of the offer, our office details etc. the back should also contain some design.
Our target market is higher end clients who own a property in Brighton and Hove and looking to sell. I would say target market 35+ years of age.
Our branding is clean, fresh and eye catching and that’s what leaflet should look like and represent.
I will insert our website link so you could have a look at the properties that we deal with too. I could also insert last leaflet which I designed and had a really positive response & feedback… maybe will give you some ideas.
I have inserted our brand guidelines. We use Hollivers in white or blue backgrounds as in guideline.
https://www.holliversestateagents.co.uk/
Hi guys,
Thank you for all your ideas so far, however just wanted to mention that I am looking for not so much ''in your face Christmas'' design - something subtle.
Needs to be classy, modern and eye catching - our target market is property owners 35+ years of age. Moreover, this offer needs to be perceived as one off opportunity.
35+ property owners

```html
<!DOCTYPE html>
<html lang="en">
<head>
<meta charset="utf-8">
<title>Hollivers Christmas Leaflet</title>
<link rel="stylesheet" href="https://fonts.googleapis.com/css2?family=Lato:wght@400;700;900&family=Great+Vibes&family=Baloo+2:wght@700;800&family=Yanone+Kaffeesatz:wght@300;500&display=swap">
<style>
  :root{
    --navy:#0c2a4b;
    --pink:#d4168e;
    --white:#ffffff;
    --stage:#525252;
    --ink:#16233a;
    --mist:#eceef1;
  }
  *{box-sizing:border-box;margin:0;padding:0}
  html,body{width:1200px;height:1200px;overflow:hidden;background:var(--stage)}
  body{position:relative;font-family:'Lato',sans-serif;color:var(--ink)}
  .leaflet{position:absolute;top:247px;width:482px;height:675px;background:var(--white);overflow:hidden}
  .leaflet--front{left:104px}
  .leaflet--back{left:615px}
  .leaflet__shapes{position:absolute;inset:0;width:482px;height:675px}
  .abs{position:absolute}

  /* front */
  .brand-badge{left:19px;top:248px;width:118px;height:118px;border-radius:50%;background:var(--navy);border:5px solid var(--pink);display:flex;align-items:center;justify-content:center}
  .brand-badge__name{font-family:'Lato',sans-serif;font-weight:700;font-size:12px;letter-spacing:2px;color:var(--white)}
  .greeting{left:22px;top:392px;font-family:'Great Vibes',cursive;font-size:44px;line-height:44px;color:var(--pink)}
  .divider{width:1.5px;background:var(--navy)}
  .front-divider{left:252px;top:374px;height:144px}
  .offer{left:276px;top:386px;width:190px}
  .offer__terms{font-size:9.6px;line-height:11.8px;color:var(--navy)}
  .offer__terms b{font-weight:900}
  .offer__headline{font-family:'Yanone Kaffeesatz',sans-serif;font-weight:300;font-size:50px;line-height:44px;color:var(--pink);margin-top:6px;letter-spacing:1px}
  .offer__sub{font-family:'Yanone Kaffeesatz',sans-serif;font-weight:500;font-style:italic;font-size:25px;line-height:24px;color:var(--pink);transform:skewX(-8deg);transform-origin:left}

  /* footer */
  .footer-hours{left:29px;color:var(--white);font-size:12.2px;line-height:14.6px}
  .footer-hours strong{font-weight:700}
  .footer-divider{background:rgba(255,255,255,.35);left:253px;height:78px}
  .footer-contact{left:273px;color:var(--white);font-size:10.8px;line-height:15.5px;font-weight:400}
  .footer-contact li{list-style:none;display:flex;align-items:center;gap:8px}
  .footer-contact svg{width:10px;height:10px;flex:none}

  /* back */
  .section-title{left:0;width:482px;top:30px;text-align:center;font-family:'Baloo 2',sans-serif;font-weight:800;font-size:20px;letter-spacing:.5px;color:var(--navy)}
  .section-title span{display:inline-block;border-bottom:3px solid var(--pink);line-height:22px;padding:0 2px 2px}
  .offer-copy{left:25px;top:70px;width:440px;font-size:12px;line-height:14.3px;color:#1c1c1c}
  .offer-copy p+p{margin-top:5px}
  .photo{left:21px;width:169px;height:134px}
  .welcome{left:207px;top:268px;width:265px}
  .welcome__title{font-family:'Baloo 2',sans-serif;font-weight:800;font-size:17.5px;line-height:20px;color:var(--pink);text-transform:uppercase;letter-spacing:.3px}
  .welcome__rule{width:55px;height:3px;background:var(--navy);margin:5px 0 14px}
  .welcome__body{font-size:12.6px;line-height:15.8px;color:#1c1c1c}
  .welcome__body p+p{margin-top:10px}
</style>
</head>
<body>

<!-- Front side -->
<section class="leaflet leaflet--front">
  <svg class="leaflet__shapes" viewBox="0 0 482 675" aria-hidden="false">
    <defs>
      <linearGradient id="frontPhoto" x1="0" y1="0" x2="0" y2="1">
        <stop offset="0" stop-color="#b9c6d4"/>
        <stop offset=".45" stop-color="#c9c2b4"/>
        <stop offset=".75" stop-color="#8aa86a"/>
        <stop offset="1" stop-color="#6fb43a"/>
      </linearGradient>
      <radialGradient id="giftGlow" cx=".5" cy=".5" r=".5">
        <stop offset="0" stop-color="#f2a6ad" stop-opacity=".55"/>
        <stop offset="1" stop-color="#f2a6ad" stop-opacity="0"/>
      </radialGradient>
    </defs>
    <rect x="0" y="0" width="482" height="340" fill="url(#frontPhoto)" role="img" aria-label="Photo of a family house with a for sale sign on the front lawn"/>
    <path d="M0 315 C150 355 330 335 482 268 V675 H0 Z" fill="var(--white)"/>
    <path d="M0 290 C150 330 330 310 482 250 L482 268 C330 335 150 355 0 315 Z" fill="var(--navy)"/>
    <ellipse cx="8" cy="450" rx="45" ry="90" fill="url(#giftGlow)" role="img" aria-label="Soft wrapped gift and bauble decoration"/>
    <ellipse cx="470" cy="440" rx="50" ry="110" fill="url(#giftGlow)" role="img" aria-label="Soft wrapped gift and bauble decoration"/>
    <path d="M0 522 C150 555 330 562 482 533 L482 548 C330 577 150 572 0 540 Z" fill="var(--pink)"/>
    <path d="M0 540 C150 572 330 577 482 548 V675 H0 Z" fill="var(--navy)"/>
  </svg>

  <div class="abs brand-badge"><span class="brand-badge__name">HOLLIVERS</span></div>

  <h1 class="abs greeting">Let us Treat you<br>&nbsp;this Christmas</h1>

  <div class="abs divider front-divider"></div>

  <div class="abs offer">
    <p class="offer__terms">If the client signs with us to sell their home from <b>1st December 2021 until 7th January 2022</b> they will receive</p>
    <p class="offer__headline">50 % OFF</p>
    <p class="offer__sub">HOLLIVERS FEES</p>
  </div>

  <div class="abs footer-hours" style="top:587px">
    <strong>Open 7 days a week</strong><br>
    Monday to Friday: 8:45am - 6:30pm<br>
    Saturday: 8:45am - 5pm<br>
    Sunday: By Appointment Only.
  </div>
  <div class="abs footer-divider" style="top:580px"></div>
  <ul class="abs footer-contact" style="top:597px">
    <li><svg viewBox="0 0 10 10"><circle cx="5" cy="5" r="4.3" fill="none" stroke="#fff" stroke-width="1"/><path d="M3.4 2.8 L4.3 3.7 L3.9 4.3 C4.3 5.1 4.9 5.7 5.7 6.1 L6.3 5.7 L7.2 6.6 L6.6 7.3 C4.9 7.1 2.9 5.1 2.7 3.4 Z" fill="#fff"/></svg>01632 480 215</li>
    <li><svg viewBox="0 0 10 10"><rect x="1" y="2.5" width="8" height="5.5" fill="#fff"/><path d="M1 2.5 L5 5.6 L9 2.5" fill="none" stroke="var(--navy)" stroke-width=".9"/></svg>sales@holliversestateagents.co.uk</li>
    <li><svg viewBox="0 0 10 10"><circle cx="5" cy="5" r="4" fill="none" stroke="#fff" stroke-width=".9"/><ellipse cx="5" cy="5" rx="1.8" ry="4" fill="none" stroke="#fff" stroke-width=".8"/><path d="M1 5 H9" stroke="#fff" stroke-width=".8"/></svg>www.holliversestateagents.co.uk</li>
  </ul>
</section>

<!-- Back side -->
<section class="leaflet leaflet--back">
  <svg class="leaflet__shapes" viewBox="0 0 482 675">
    <defs>
      <linearGradient id="backMist" x1="0" y1="0" x2="0" y2="1">
        <stop offset="0" stop-color="#f6f6f7"/>
        <stop offset="1" stop-color="#e3e4e7"/>
      </linearGradient>
      <linearGradient id="handPhoto" x1="0" y1="0" x2="1" y2="1">
        <stop offset="0" stop-color="#1d3552"/>
        <stop offset=".55" stop-color="#2a3f5c"/>
        <stop offset="1" stop-color="#0f1e33"/>
      </linearGradient>
      <linearGradient id="homePhoto" x1="0" y1="0" x2="0" y2="1">
        <stop offset="0" stop-color="#4d95dc"/>
        <stop offset=".5" stop-color="#a7b3bb"/>
        <stop offset="1" stop-color="#5c9b3a"/>
      </linearGradient>
      <radialGradient id="giftGlowBack" cx=".5" cy=".5" r=".5">
        <stop offset="0" stop-color="#f2a6ad" stop-opacity=".45"/>
        <stop offset="1" stop-color="#f2a6ad" stop-opacity="0"/>
      </radialGradient>
    </defs>
    <rect x="0" y="0" width="482" height="240" fill="url(#backMist)" role="img" aria-label="Faded winter photo of a house with a for sale sign"/>
    <path d="M0 222 C150 252 330 250 482 212 V675 H0 Z" fill="var(--white)"/>
    <path d="M0 210 C150 240 330 236 482 198 L482 212 C330 250 150 252 0 222 Z" fill="var(--pink)"/>
    <ellipse cx="462" cy="430" rx="45" ry="110" fill="url(#giftGlowBack)" role="img" aria-label="Soft wrapped gift and bauble decoration"/>
    <rect x="21" y="261" width="169" height="134" fill="url(#handPhoto)" role="img" aria-label="Photo of a hand holding a model house"/>
    <rect x="21" y="403" width="169" height="134" fill="url(#homePhoto)" role="img" aria-label="Photo of a large family home with a landscaped garden"/>
    <path d="M0 525 C150 555 330 560 482 525 L482 540 C330 577 150 572 0 542 Z" fill="var(--pink)"/>
    <path d="M0 542 C150 572 330 577 482 540 V675 H0 Z" fill="var(--navy)"/>
  </svg>

  <h2 class="abs section-title"><span>ABOUT THE OFFER</span></h2>

  <div class="abs offer-copy">
    <p>Lorem ipsum dolor sit amet, consectetur adipiscing elit, sed do eiusmod tempor incididunt ut labore et dolore magna aliqua. Ut enim ad minim veniam, quis nostrud exercitation ullamco laboris nisi ut aliquip ex ea commodo consequat.</p>
    <p>Lorem ipsum dolor sit amet, consectetur adipiscing elit, sed do eiusmod tempor incididunt ut labore et dolore magna aliqua.</p>
    <p style="margin-top:9px">Lorem ipsum dolor sit amet, consectetur adipiscing elit, sed do eiusmod tempor incididunt ut labore et dolore magna aliqua. Ut enim ad minim veniam, quis nostrud exercitation ullamco laboris nisi ut aliquip ex ea commodo consequat.</p>
  </div>

  <div class="abs welcome">
    <h3 class="welcome__title">Welcome to Brighton &amp;<br>Hove's trusted estate agent</h3>
    <div class="welcome__rule"></div>
    <div class="welcome__body">
      <p>Hollivers is a modern, independent estate agency specialising in residential sales within Brighton and Hove.</p>
      <p>Whether you are looking to buy, sell, let or rent a property our highly experienced team are on hand to help you through the whole process.</p>
      <p>We offer a wide range of properties from boutique seaside apartments, townhouses to larger family or luxury properties across Brighton and Hove.</p>
    </div>
  </div>

  <div class="abs footer-hours" style="top:584px;left:29px">
    <strong>Open 7 days a week</strong><br>
    Monday to Friday: 8:45am - 6:30pm<br>
    Saturday: 8:45am - 5pm<br>
    Sunday: By Appointment Only.
  </div>
  <div class="abs footer-divider" style="top:582px;left:239px"></div>
  <ul class="abs footer-contact" style="top:592px;left:257px">
    <li><svg viewBox="0 0 10 10"><circle cx="5" cy="5" r="4.3" fill="none" stroke="#fff" stroke-width="1"/><path d="M3.4 2.8 L4.3 3.7 L3.9 4.3 C4.3 5.1 4.9 5.7 5.7 6.1 L6.3 5.7 L7.2 6.6 L6.6 7.3 C4.9 7.1 2.9 5.1 2.7 3.4 Z" fill="#fff"/></svg>01632 480 215</li>
    <li><svg viewBox="0 0 10 10"><rect x="1" y="2.5" width="8" height="5.5" fill="#fff"/><path d="M1 2.5 L5 5.6 L9 2.5" fill="none" stroke="var(--navy)" stroke-width=".9"/></svg>sales@holliversestateagents.co.uk</li>
    <li><svg viewBox="0 0 10 10"><circle cx="5" cy="5" r="4" fill="none" stroke="#fff" stroke-width=".9"/><ellipse cx="5" cy="5" rx="1.8" ry="4" fill="none" stroke="#fff" stroke-width=".8"/><path d="M1 5 H9" stroke="#fff" stroke-width=".8"/></svg>www.holliversestateagents.co.uk</li>
  </ul>
</section>

</body>
</html>
```